Cinq Leviers SEO Zorvana Plumea ebook cover (2nd of book series) *

Book Title :
Cinq Leviers pour muscler votre Visibilité Organique SEO

Or alternatively if design is better :
SEO : Cinq Leviers pour muscler votre Visibilité Organique

Subtitle : Comment hisser votre page au sommet des annuaires du web

Subject : The book is a very practical how-to guide to help anyone increase dramatically their trafic through SEO (Search Engine Opimization)

It is written in French : so please keep punctuation as provided

The book cover MUST STAND OUT on the Zorvana Plateform as a small Thumbnail (The important words must be readable even at that size : CINQ LEVIERS, Visibilité Organique, SEO) as well as a 6*9 book.

The imagery should make the viewer feel that the book (and the author) are the authority in Search Engine Optimization and Digital Marketing

The readers should feel that they must have this book to increase their site or blog traffic fast.

It is most important that the book “pops off the shelf” and catches the eye quickly. The most important part of the design is that it sells, not that it looks pretty (but it can :-)

Important thing : this cover and ebook is part of a series of books all titled “Cinq Leviers blablabla”. There is already one book of this series published (see cover 5) : Cinq Leviers pour Doubler vos Gains. It’s important that at least one element of this new design recalls the design of the Cover 5 It can be for example the typo for the “7” being the same, or any other idea so that when someone sees both covers, they understand they are from the same series.

I have also enclosed my attempt so that you get the idea I am after, but don’t be too close to it. I am not a designer and I know it is bad, so be free, it is just here to explain the idea of the book cover.
Attached are some covers :
 Covers 1 to 4 are covers I like very much
 Cover 5 is from The first book of the Series : “Cinq Leviers pour Doubler vos Gains” : there should be at least ONE (even tiny) element in common with the new design so that it’s clear they belong to the same series
 Cover 6 is my ugly attempt so that the idea is clear (hopefully)

Target Market(s)

Small entrepreneurs bloggers

Font styles to use
Sans Serif

Colors

Designer to choose colors to be used in the design.

Requirements
Must have
• The book cover MUST STAND OUT on the Zorvana Plateform as a small Thumbnail (The important must be readable even at that size : CINQ LEVIERS, Visibilité Organique, SEO) as well as a 6*9 book.
• Important thing : this cover and ebook is part of a series of books all titled “Cinq Leviers blablabla”. There is already one book of this series published (see cover 5) : Cinq Leviers pour Doubler vos Gains. It’s important that at least one element of this new design recalls the design of the Cover 5 It can be for example the typo for the “7” being the same, or any other idea so that when someone sees both covers, they understand they are from the same series.
• All the texts provided on the brief and my sample cover (6th cover mockup)
• Please enclose the text :
• Checklist SEO Incluse
• In a sticker (see last image as example)
Nice to have
• Nice and simple imagery. Like the one on Cart Sparks. Very simple but also very powerful and meaningful
Should not have
• It should not be as cluttered as my attempt (6th cover enclosed)

```html
<!DOCTYPE html>
<html lang="fr">
<head>
<meta charset="utf-8">
<title>Cinq Leviers pour muscler votre Visibilité Organique SEO</title>
<link rel="stylesheet" href="https://fonts.googleapis.com/css2?family=Source+Sans+3:wght@400;600;700&display=swap">
<style>
  :root {
    --page-bg: #e4e9ec;
    --cover-bg: #ffffff;
    --title-orange: #f08c00;
    --band-orange: #ff7f00;
    --brand-green: #00734f;
    --band-text: #3b3a2c;
    --sticker-text: #ffffff;
    --art-light: #f4f4f4;
    --art-orange: #ffb000;
    --art-deep: #f07800;
  }
  * { margin: 0; padding: 0; box-sizing: border-box; }
  html, body {
    width: 1200px;
    height: 1200px;
    overflow: hidden;
    background: var(--page-bg);
    font-family: "Source Sans 3", "Myriad Pro", Arial, sans-serif;
  }
  .book-cover {
    position: absolute;
    left: 272px;
    top: 126px;
    width: 656px;
    height: 982px;
    background: var(--cover-bg);
    text-align: center;
  }
  .cover-art {
    position: absolute;
    left: 164px;
    top: 109px;
    width: 268px;
    height: 250px;
    border-radius: 4px;
    background: linear-gradient(120deg, var(--art-light) 0%, var(--art-light) 35%, var(--art-orange) 62%, var(--art-deep) 100%);
  }
  .checklist-sticker {
    position: absolute;
    left: 478px;
    top: 150px;
    width: 140px;
    height: 140px;
    border-radius: 50%;
    background: var(--brand-green);
    color: var(--sticker-text);
    display: flex;
    align-items: center;
    justify-content: center;
    font-weight: 700;
    font-size: 21px;
    line-height: 24px;
    text-transform: uppercase;
    transform: rotate(-10deg);
  }
  .title-block {
    position: absolute;
    left: 0;
    right: 0;
    top: 398px;
  }
  .title-lead {
    display: block;
    color: var(--title-orange);
    font-weight: 700;
    font-size: 78px;
    line-height: 80px;
    letter-spacing: -0.5px;
  }
  .title-line {
    display: block;
    color: var(--brand-green);
    font-weight: 400;
    font-size: 44px;
    line-height: 53px;
    letter-spacing: -1px;
  }
  .title-line--strong { font-weight: 700; }
  .subtitle-band {
    position: absolute;
    left: 0;
    right: 0;
    top: 666px;
    height: 105px;
    background: var(--band-orange);
    display: flex;
    align-items: center;
    justify-content: center;
  }
  .subtitle {
    color: var(--band-text);
    font-size: 22px;
    line-height: 27px;
    text-transform: uppercase;
    letter-spacing: -0.5px;
  }
  .author {
    position: absolute;
    left: 0;
    right: 0;
    top: 862px;
    color: var(--brand-green);
    font-size: 60px;
    line-height: 68px;
    font-weight: 400;
    letter-spacing: -1.5px;
  }
  .author strong { font-weight: 700; }
</style>
</head>
<body>
  <main class="book-cover">
    <div class="cover-art" role="img" aria-label="Peeled-paper cut-out lettering revealing a bright orange layer beneath a curling white page"></div>

    <p class="checklist-sticker">Checklist<br>SEO<br>Incluse</p>

    <h1 class="title-block">
      <span class="title-lead">Cinq Leviers</span>
      <span class="title-line">POUR MUSCLER</span>
      <span class="title-line">VOTRE VISIBILITÉ</span>
      <span class="title-line title-line--strong">ORGANIQUE SEO</span>
    </h1>

    <div class="subtitle-band">
      <p class="subtitle">Comment hisser votre page au sommet<br>des annuaires du web</p>
    </div>

    <p class="author">AUTHOR <strong>NAME</strong></p>
  </main>
</body>
</html>
```